QuillMark Business Cards

I need a business card designed for QuillMark. To get an idea of what we do please visit https://formvault.example/para-creadores-3

```html
<!DOCTYPE html>
<html lang="en">
<head>
<meta charset="utf-8">
<title>QuillMark Business Cards</title>
<link rel="stylesheet" href="https://fonts.googleapis.com/css2?family=Arimo:wght@400;700&display=swap">
<style>
  :root {
    --backdrop: #e4921b;
    --card: #1b1d22;
    --accent: #e4921b;
    --accent-deep: #cd7408;
    --ink: #ffffff;
  }
  html, body {
    margin: 0;
    padding: 0;
    width: 1200px;
    height: 1200px;
    overflow: hidden;
    background: var(--backdrop);
    font-family: "Arimo", Arial, sans-serif;
  }
  .card {
    position: absolute;
    background: var(--card);
    overflow: hidden;
    color: var(--ink);
  }
  .card--front { left: 267px; top: 170px; width: 684px; height: 388px; }
  .card--back  { left: 266px; top: 666px; width: 682px; height: 384px; }

  .pattern-area {
    position: absolute;
    right: 0;
    bottom: 0;
  }
  .card--front .pattern-area { width: 380px; height: 240px; }
  .card--back .pattern-area  { width: 380px; height: 240px; }

  .brand-name {
    position: absolute;
    margin: 0;
    font-weight: 400;
    color: var(--ink);
    white-space: nowrap;
  }
  .brand-tagline {
    position: absolute;
    margin: 0;
    color: var(--accent);
    white-space: nowrap;
    display: flex;
    align-items: center;
  }
  .brand-tagline::after {
    content: "";
    display: block;
    height: 1px;
    background: var(--ink);
    margin-left: 4px;
  }

  .card--front .brand-name {
    left: 168px; top: 148px;
    font-size: 30px; letter-spacing: 11px;
  }
  .card--front .brand-tagline {
    left: 170px; top: 186px;
    font-size: 9px; letter-spacing: 5.5px;
  }
  .card--front .brand-tagline::after { width: 104px; }

  .card--back .brand-name {
    left: 487px; top: 53px;
    font-size: 20px; letter-spacing: 6.5px;
  }
  .card--back .brand-tagline {
    left: 488px; top: 78px;
    font-size: 6px; letter-spacing: 3.3px;
  }
  .card--back .brand-tagline::after { width: 66px; }

  .person-name {
    position: absolute;
    left: 38px; top: 44px;
    margin: 0;
    font-size: 30px;
    font-weight: 400;
    white-space: nowrap;
  }
  .person-name strong { font-weight: 700; }
  .person-role {
    position: absolute;
    left: 39px; top: 78px;
    margin: 0;
    font-size: 18px;
  }
  .name-rule {
    position: absolute;
    left: 41px; top: 109px;
    width: 254px; height: 3px;
    background: var(--ink);
  }
  .name-rule::before {
    content: "";
    position: absolute;
    left: 0; top: -1px;
    width: 52px; height: 5px;
    background: var(--accent);
  }

  .contact-list {
    position: absolute;
    left: 34px; top: 148px;
    margin: 0; padding: 0;
    list-style: none;
  }
  .contact-list li {
    display: flex;
    align-items: center;
    height: 36px;
    font-size: 18px;
  }
  .contact-list svg { width: 22px; height: 22px; margin-right: 12px; fill: var(--ink); }

  .address {
    position: absolute;
    left: 51px; top: 290px;
    margin: 0;
    font-style: normal;
    font-size: 17px;
    line-height: 22px;
  }
</style>
</head>
<body>
  <section class="card card--front" aria-label="Card front">
    <svg class="pattern-area" role="img" aria-label="Decorative triangle mosaic fading in from the corner" viewBox="0 0 380 240" preserveAspectRatio="none">
      <defs>
        <radialGradient id="mosaic-front" cx="1" cy="1" r="1.1">
          <stop offset="0" stop-color="#cd7408" stop-opacity="0.95"/>
          <stop offset="0.45" stop-color="#cd7408" stop-opacity="0.55"/>
          <stop offset="1" stop-color="#cd7408" stop-opacity="0"/>
        </radialGradient>
      </defs>
      <rect width="380" height="240" fill="url(#mosaic-front)"/>
    </svg>
    <h1 class="brand-name">QUILLMARK</h1>
    <p class="brand-tagline">DIGITAL NOTARY</p>
  </section>

  <section class="card card--back" aria-label="Card back">
    <svg class="pattern-area" role="img" aria-label="Decorative triangle mosaic fading in from the corner" viewBox="0 0 380 240" preserveAspectRatio="none">
      <defs>
        <radialGradient id="mosaic-back" cx="1" cy="1" r="1.1">
          <stop offset="0" stop-color="#cd7408" stop-opacity="0.95"/>
          <stop offset="0.45" stop-color="#cd7408" stop-opacity="0.55"/>
          <stop offset="1" stop-color="#cd7408" stop-opacity="0"/>
        </radialGradient>
      </defs>
      <rect width="380" height="240" fill="url(#mosaic-back)"/>
    </svg>

    <h2 class="person-name"><strong>NAME</strong> SURNAME</h2>
    <p class="person-role">POSITION</p>
    <div class="name-rule"></div>

    <ul class="contact-list">
      <li>
        <svg viewBox="0 0 24 24" aria-hidden="true"><path d="M6.6 2.5l3 3.6c.4.5.4 1.2 0 1.7L7.9 9.6c1.3 2.8 3.7 5.2 6.5 6.5l1.8-1.7c.5-.4 1.2-.4 1.7 0l3.6 3c.5.4.6 1.2.1 1.7l-1.6 1.9c-.6.7-1.6 1-2.5.7C10.6 19.6 4.4 13.4 2.3 6.5c-.3-.9 0-1.9.7-2.5L4.9 2.4c.5-.5 1.3-.4 1.7.1z"/></svg>
        +00-000-000
      </li>
      <li>
        <svg viewBox="0 0 24 24" aria-hidden="true"><path d="M1 5h22v14H1z M3 7v10l6-5z M21 7l-6 5 6 5z M4 6.5l8 6.5 8-6.5z M10.5 13.2L4.5 18h15l-6-4.8-1.5 1.2z"/></svg>
        INFO@QUILLMARK.
      </li>
      <li>
        <svg viewBox="0 0 24 24" aria-hidden="true"><path d="M5 2l13 12-6 .6 3.6 7-2.4 1.2-3.5-7L5 20z"/></svg>
        WWW.QUILLMARK.
      </li>
    </ul>

    <address class="address">
      123 LOCATION HERE<br>
      STREET<br>
      POSTAL 0000
    </address>

    <p class="brand-name">QUILLMARK</p>
    <p class="brand-tagline">DIGITAL NOTARY</p>
  </section>
</body>
</html>
```